Harbor Lantern Podcast needs fun, creative cover art

Launching a new podcast called 'Opening Windows Toward Brighter Days' - aimed at an audience 30-50 who are interested in the practicalities of managing their money but also the more mental and emotional aspects.
Looking for something not too serious, warm and friendly.

Must be easy to read on phone screens
3000 x 3000 in size
Avoid currency symbols $, £ etc, as may have an international audience

Target Market(s)

Podcast listeners age 30-50 starting in the UK but then worldwide. Probably 60:40 female bias

Industry/Entity Type

Life Coaching

Font styles to use
Serif
Sans Serif

Colors
cadf82
fee18a
acd037
85cae6
eea4c8
f59195
85acd3

Requirements
Must have
• Simple, clear design. Easy to read on variety of devices. 3000 x 3000
Appeal to those with a spiritual or emotional interests
Nice to have
• Stand out among other money related podcasts
Maybe play around with clouds, lightbulbs and clearing skies
Should not have
• Currency symbols such as $ or £
Be too corporate or bank like
Stock images

```html
<!DOCTYPE html>
<html lang="en">
<head>
<meta charset="utf-8">
<title>Harbor Lantern Podcast — Cover Art Samples</title>
<link rel="stylesheet" href="https://fonts.googleapis.com/css2?family=Montserrat:wght@500;800&family=Oswald:wght@400&display=swap">
<style>
  :root {
    --board: #1f1f1f;
    --header: #000000;
    --ink-light: #ffffff;
    --head-dark: #2f2f2f;
    --lime: #acd037;
    --lime-soft: #cadf82;
    --butter: #fee18a;
    --coral: #f59195;
    --rose: #eea4c8;
    --sky: #85cae6;
    --denim: #85acd3;
  }
  * { margin: 0; padding: 0; box-sizing: border-box; }
  html, body { width: 1200px; height: 2244px; overflow: hidden; }
  body { background: var(--board); position: relative; font-family: "Montserrat", sans-serif; }

  .board-header {
    position: absolute; left: 0; top: 0; width: 1200px; height: 118px;
    background: var(--header); display: flex; align-items: center; justify-content: center;
  }
  .board-title {
    color: var(--ink-light); font: 500 26px "Montserrat", sans-serif; letter-spacing: 0.42em;
  }

  .sample-label {
    position: absolute; left: 47px; color: var(--ink-light);
    font: 500 16px "Montserrat", sans-serif; letter-spacing: 0.32em;
  }

  .cover { position: absolute; left: 47px; width: 545px; height: 545px; overflow: hidden; }
  .cover-art { position: absolute; inset: 0; width: 545px; height: 545px; display: block; }

  .title { position: absolute; line-height: 1; }
  .title span { display: block; }
  .title .lead { font: 400 48px "Oswald", sans-serif; color: var(--ink-light); }
  .title .big { font: 800 70px "Montserrat", sans-serif; color: var(--lime); line-height: 0.95; letter-spacing: -0.02em; }
  .title .tail { font: 400 58px "Oswald", sans-serif; color: var(--ink-light); margin-top: 6px; }
  .title .accent { color: var(--sky); }

  .cover--one { top: 216px; }
  .cover--one .title { left: 112px; top: 82px; }
  .cover--one .lead { letter-spacing: 0.32em; }

  .cover--two { top: 926px; }
  .cover--two .title { right: 52px; top: 100px; text-align: right; }

  .cover--three { top: 1630px; }
  .cover--three .title { right: 30px; top: 84px; text-align: right; }
  .cover--three .big, .cover--three .lead, .cover--three .tail { color: var(--ink-light); }
</style>
</head>
<body>
  <header class="board-header">
    <h1 class="board-title">HARBOR LANTERN PODCAST _3000 X 3000</h1>
  </header>

  <p class="sample-label" style="top:178px">SAMPLE 1</p>
  <section class="cover cover--one">
    <svg class="cover-art" viewBox="0 0 545 545" role="img" aria-label="Head silhouette in profile with layered lime outline on a coral background">
      <rect width="545" height="545" fill="var(--coral)"/>
      <path d="M40,545 L40,250 Q40,0 300,0 L545,0 L545,545 Z" fill="var(--lime)"/>
      <path d="M75,545 L75,265 Q75,35 305,35 Q470,35 545,190 L545,545 Z" fill="var(--coral)"/>
      <path d="M95,545 L95,270 Q95,55 310,55 Q460,55 545,210 L545,545 Z" fill="var(--head-dark)"/>
    </svg>
    <h2 class="title">
      <span class="lead">OPENING</span>
      <span class="big">WINDOWS</span>
      <span class="big">TOWARD</span>
      <span class="tail">BRIGHTER <span class="accent" style="display:inline">DAYS</span></span>
    </h2>
  </section>

  <p class="sample-label" style="top:884px">SAMPLE 2</p>
  <section class="cover cover--two">
    <svg class="cover-art" viewBox="0 0 545 545" role="img" aria-label="Three stacked head silhouettes in yellow, coral and charcoal on a blue background">
      <rect width="545" height="545" fill="var(--denim)"/>
      <path d="M0,545 L0,330 Q20,40 280,45 L545,45 L545,545 Z" fill="var(--butter)"/>
      <path d="M45,545 L45,330 Q65,45 320,45 L545,45 L545,545 Z" fill="var(--coral)"/>
      <path d="M95,545 L95,330 Q115,45 380,45 Q545,60 545,230 L545,545 Z" fill="var(--head-dark)"/>
    </svg>
    <h2 class="title">
      <span class="lead">OPENING</span>
      <span class="big">WINDOWS</span>
      <span class="big">TOWARD</span>
      <span class="tail">BRIGHTER <span class="accent" style="display:inline">DAYS</span></span>
    </h2>
  </section>

  <p class="sample-label" style="top:1592px">SAMPLE 3</p>
  <section class="cover cover--three">
    <svg class="cover-art" viewBox="0 0 545 545" role="img" aria-label="Cloudy blue sky photograph filling a head silhouette, with dark layered profiles on the left">
      <defs>
        <linearGradient id="sky-fill" x1="0" y1="0" x2="1" y2="1">
          <stop offset="0" stop-color="#dde6ef"/>
          <stop offset="0.5" stop-color="#7f9fc8"/>
          <stop offset="1" stop-color="#c9d6e6"/>
        </linearGradient>
      </defs>
      <rect width="545" height="545" fill="url(#sky-fill)"/>
      <path d="M0,0 L210,0 Q90,150 100,300 Q110,450 260,545 L0,545 Z" fill="#2a1c1c"/>
      <path d="M0,0 L190,0 Q70,150 80,300 Q90,450 235,545 L0,545 Z" fill="#111111"/>
    </svg>
    <h2 class="title">
      <span class="lead">OPENING</span>
      <span class="big">WINDOWS</span>
      <span class="big">TOWARD</span>
      <span class="tail">BRIGHTER DAYS</span>
    </h2>
  </section>
</body>
</html>
```